Technical Communications firm needs an article turned into a white paper

We want to redesign a 3-part blog series into a white paper that we can print for a conference. I've consolidated the three posts into the attached Word document.

We are looking for a light, easy to read design. Good use of graphics to support the message. I've added the graphics we used in the original post.

You can view them at
http://www.quillmarrowgroup.com/blog/are-you-satisfied-with-your-dita-solution/

Target Market(s)

Product managers from High-tech, Finance, and Medical industries.

Industry/Entity Type

Information Technology

Colors

Designer to choose colors to be used in the design.

Requirements
Must have
• Must be modern, light, easy to read and slick design. Try to incorporate the graphics provided, but feel free to add more. Must retain the lists and tables.
• Must align with our website/brand.
• Must be easy to read. So not too busy.
• Please move all footnotes to endnotes. You'll need to rework the numbering.
Nice to have
• Awesome coverpage.
Should not have
• Hokey clipart. Not too heavy or hard to read.

```html
<!DOCTYPE html>
<html lang="en">
<head>
<meta charset="utf-8">
<title>Unlock the Knowledge in Your Enterprise — White Paper</title>
<link href="https://fonts.googleapis.com/css2?family=Exo+2:wght@500;600;700&family=Open+Sans:wght@400;600;700&display=swap" rel="stylesheet">
<style>
  :root {
    --stage: #e9e7e4;
    --paper: #ffffff;
    --navy: #1a1f9c;
    --royal: #1f4fd1;
    --sky: #1a9ad6;
    --ink: #2a2a2a;
    --muted: #555;
    --dark-box: #3a3a3c;
  }
  * { box-sizing: border-box; margin: 0; padding: 0; }
  html, body { width: 1200px; height: 1200px; overflow: hidden; background: var(--stage); }
  body { position: relative; font-family: "Open Sans", sans-serif; color: var(--ink); }

  .page { position: absolute; width: 350px; height: 490px; background: var(--paper); box-shadow: 0 6px 18px rgba(0,0,0,.25); overflow: hidden; }
  .cover { left: 425px; top: 76px; }
  .page-one { left: 151px; top: 642px; }
  .page-two { left: 719px; top: 642px; }

  /* Cover */
  .cover-hero { position: absolute; inset: 0 0 132px 0; background: linear-gradient(160deg, #1d8fe0 0%, #1f5fd8 45%, #1e2fb0 100%); overflow: hidden; }
  .brand { position: absolute; left: 186px; top: 26px; display: flex; align-items: center; gap: 6px; color: #fff; font-family: "Exo 2", sans-serif; font-weight: 700; font-size: 13px; line-height: 1.05; }
  .brand-dot { width: 26px; height: 26px; border-radius: 50%; border: 3px solid #fff; flex: none; }
  .cover-bubbles { position: absolute; left: 0; top: 0; width: 350px; height: 376px; }
  .cover-title { position: absolute; left: 0; right: 0; top: 388px; text-align: center; font-family: "Exo 2", sans-serif; font-weight: 700; line-height: 1.1; }
  .cover-title .kicker { display: block; color: var(--sky); font-size: 24px; letter-spacing: .5px; }
  .cover-title .main { display: block; color: var(--navy); font-size: 29px; font-weight: 600; }
  .cover-url { position: absolute; left: 0; right: 0; top: 470px; text-align: center; font-size: 5.5px; letter-spacing: 1.4px; color: #333; }

  /* Inner pages */
  .top-band { position: absolute; left: 0; right: 0; top: 0; height: 7px; background: var(--navy); }
  .content { position: absolute; left: 21px; right: 21px; top: 20px; }
  .h-section { font-family: "Exo 2", sans-serif; font-weight: 700; color: var(--sky); font-size: 11px; letter-spacing: .2px; margin-bottom: 4px; }
  .byline { font-size: 5px; margin-bottom: 6px; }
  .byline strong { font-weight: 700; }
  .body { font-size: 5px; line-height: 1.38; color: var(--muted); margin-bottom: 4px; }

  .issue-bar { display: flex; justify-content: space-between; background: var(--dark-box); border-radius: 3px; height: 46px; padding: 7px 10px 0; margin: 8px 0 10px; }
  .issue { display: flex; flex-direction: column; align-items: center; gap: 4px; color: #fff; font-family: "Exo 2", sans-serif; font-weight: 700; font-size: 7px; }
  .issue-icon { width: 18px; height: 18px; border-radius: 50%; background: #fff; display: flex; align-items: center; justify-content: center; }
  .issue-icon span { width: 11px; height: 11px; border-radius: 50%; background: var(--sky); }

  .part-pill { display: inline-flex; align-items: center; gap: 6px; border: 1px solid #777; border-radius: 10px; height: 19px; padding: 0 8px 0 0; margin: 5px 0 3px; font-family: "Exo 2", sans-serif; font-weight: 700; font-size: 10px; color: var(--sky); }
  .part-pill .letter { width: 19px; height: 19px; margin-left: -1px; border-radius: 50%; background: var(--dark-box); color: #fff; display: flex; align-items: center; justify-content: center; font-size: 11px; }
  .part-pill .label { color: var(--navy); }

  .endnote-box { position: absolute; left: 21px; right: 21px; top: 424px; height: 38px; border: 1px solid #888; border-radius: 5px; padding: 4px 6px; font-size: 5px; line-height: 1.35; color: var(--muted); }

  .footer { position: absolute; left: 0; bottom: 0; width: 350px; height: 19px; }
  .footer-num { position: absolute; left: 24px; bottom: 4px; color: #fff; font-size: 8px; font-weight: 700; }
  .footer-url { position: absolute; right: 24px; bottom: 6px; color: #fff; font-size: 5px; }

  .page-two .h-section.centered { text-align: center; margin-bottom: 12px; }
  .issue-list { list-style: none; margin-bottom: 4px; }
  .issue-list li { font-size: 5px; line-height: 1.9; font-weight: 600; color: var(--ink); display: flex; align-items: center; gap: 3px; }
  .issue-list li::before { content: ""; width: 4px; height: 4px; border-radius: 50%; border: 1px solid var(--sky); }
  .page-photo { position: absolute; left: 0; right: 0; top: 323px; bottom: 0; background: linear-gradient(100deg, #c9d3df 0%, #e9eef3 35%, #b9c3cf 65%, #7f97b7 100%); }
</style>
</head>
<body>

<!-- Cover -->
<section class="page cover">
  <div class="cover-hero" role="img" aria-label="Blue gradient background with a faint technical line pattern">
    <div class="brand"><span class="brand-dot"></span><span>QUILL MARROW<br>GROUP</span></div>
  </div>
  <svg class="cover-bubbles" viewBox="0 0 350 376">
    <g fill="none" stroke="#fff" stroke-width="3">
      <circle cx="257" cy="154" r="60"/>
      <circle cx="161" cy="254" r="52"/>
      <circle cx="254" cy="299" r="45"/>
    </g>
    <defs>
      <radialGradient id="tech" cx=".5" cy=".45" r=".6"><stop offset="0" stop-color="#e3e8ee"/><stop offset="1" stop-color="#5c6f86"/></radialGradient>
      <radialGradient id="city" cx=".5" cy=".6" r=".6"><stop offset="0" stop-color="#6fb6f0"/><stop offset="1" stop-color="#1d2b6a"/></radialGradient>
      <radialGradient id="office" cx=".5" cy=".5" r=".6"><stop offset="0" stop-color="#f1ece4"/><stop offset="1" stop-color="#8d8c88"/></radialGradient>
    </defs>
    <circle cx="257" cy="154" r="52" fill="url(#tech)" role="img" aria-label="Photo: open hand holding floating cloud and device icons"/>
    <circle cx="161" cy="254" r="45" fill="url(#city)" role="img" aria-label="Photo: glowing digital data dashboard"/>
    <circle cx="254" cy="299" r="38" fill="url(#office)" role="img" aria-label="Photo: business team around a tablet showing a bar chart"/>
  </svg>
  <h1 class="cover-title"><span class="kicker">UNLOCK THE KNOWLEDGE</span><span class="main">IN YOUR ENTERPRISE</span></h1>
  <p class="cover-url">www.quillmarrowgroup.com</p>
</section>

<!-- Page 1 -->
<section class="page page-one">
  <div class="top-band"></div>
  <div class="content">
    <h2 class="h-section">ARE YOU SATISFIED WITH YOUR DITA SOLUTION?</h2>
    <p class="byline">By Dana Whitlock – President of Quill Marrow Authoring Solutions Inc.</p>
    <p class="body">If your answer is “No” then you are not alone according to a 2017 survey of more than 250 technical communication professionals conducted by The Docs Roundup. The DITA Satisfaction Survey[i] indicates that 62% of respondents using DITA are—to varying degrees—dissatisfied. As many as 10% of that group were very dissatisfied reporting that their DITA implementation is experiencing ‘big’ challenges. It’s not surprising that there’s significant dissatisfaction amongst those who have adopted DITA. After all, moving to DITA is a seismic shift in technical writing; a big change with many opportunities for things to go wrong.</p>
    <p class="body">The good news is that most DITA users don’t see their problems as insurmountable. Many just need a little help getting to where they’d like to be.</p>
    <h2 class="h-section" style="margin-top:7px">BREAKDOWN OF THE ISSUES</h2>
    <p class="body">The Docs Roundup DITA Satisfaction Survey asked respondents to rank the top 10 issues facing DITA users. These issues fit into three major categories including</p>
    <div class="issue-bar">
      <div class="issue"><span class="issue-icon"><span></span></span>SKILLS DEVELOPMENT</div>
      <div class="issue"><span class="issue-icon"><span></span></span>TECHNOLOGY</div>
      <div class="issue"><span class="issue-icon"><span></span></span>MANAGEMENT</div>
    </div>
    <p class="body">The DITA Satisfaction Survey Aggregate Results revealed little spread between the ranking of the issues indicating that respondents likely faced more than one issue of concern.</p>
    <h2 class="h-section" style="margin-top:6px">IN THIS ARTICLE</h2>
    <p class="body">In this article, we examine three issues impacting DITA satisfaction to help you find the best place to start making improvements.</p>
    <div class="part-pill"><span class="letter">A</span><span>PART 1: <span class="label">SKILLS DEVELOPMENT</span></span></div>
    <p class="body">This problem area is far and away the most pressing obstacle for a successful DITA deployment. Too often authors are left to figure out how to adapt to writing for DITA on their own.</p>
    <div class="part-pill"><span class="letter">B</span><span>PART 2: <span class="label">TECHNOLOGY</span></span></div>
    <p class="body">We often hear about the failure of the technology as it relates to performance or complexity. While technology may seem the most likely culprit, it is often not the root cause of the problem.</p>
    <div class="part-pill"><span class="letter">C</span><span>PART 3: <span class="label">MANAGEMENT</span></span></div>
    <p class="body">While these issues appear to be of least concern to many survey respondents, they are most likely to form the root cause of all other issues identified in the survey. This points to a general lack of awareness as to the role management should be playing in collaborative, structured authoring solutions.</p>
  </div>
  <div class="endnote-box">[i] DITA Satisfaction Survey published by The Docs Roundup on May 31, 2017. Listen to an analysis of the results by Dana Whitlock, Omar Lindqvist, Priya Castell and Jonah Breck and download a copy of the results today from WebinarHub at https://www.webinarhub.com/webcast/9273/259775</div>
  <svg class="footer" viewBox="0 0 350 19" aria-hidden="true">
    <polygon points="0,0 52,0 66,19 0,19" fill="var(--navy)"/>
    <polygon points="222,0 350,0 350,19 208,19" fill="var(--navy)"/>
  </svg>
  <span class="footer-num">1</span>
  <span class="footer-url">www.quillmarrowgroup.com</span>
</section>

<!-- Page 2 -->
<section class="page page-two">
  <div class="top-band"></div>
  <div class="content" style="top:22px">
    <h2 class="h-section centered">PART 1: SKILLS DEVELOPMENT</h2>
    <p class="byline"><strong>By Dana Whitlock – President of Quill Marrow Group</strong></p>
    <p class="body">This article is part of a series based on the results of a survey of more than 250 technical communication professionals conducted by The Docs Roundup in 2017 entitled The DITA Satisfaction Survey[i]. In the survey, almost two-thirds of respondents voiced concerns with their DITA deployment.</p>
    <p class="body">In our previous article, we introduced the overall results from the survey that pertain to users’ dissatisfaction with their DITA solution. In this article, we examine the top rated issues pertaining to skills development.</p>
    <h2 class="h-section" style="margin-top:6px">ISSUES RELATED TO SKILLS DEVELOPMENT</h2>
    <p class="body">The top-ranked reported issues fall under the category of skill development and training. These include</p>
    <ul class="issue-list">
      <li>How do I reuse content? Ranked 1st by 75% of respondents</li>
      <li>How do I make DITA do what I want it to do? Ranked 2nd by 69% of respondents</li>
      <li>Where can I get DITA training? Ranked 3rd by 64% of respondents, and</li>
      <li>How do I create DITA content? Ranked 8th by 56% of respondents.</li>
    </ul>
    <p class="body">This problem area is far and away the most pressing obstacle for a successful DITA deployment. Too often authors are left to figure out how to adapt to writing for DITA on their own. Organizations will normally invest in tools training—and may even opt for a short training course to learn about DITA—but they rarely make the effort to train writers how to author modular, structured topics of content designed for reuse. It is easy to overlook this training aspect and assume that writers will naturally adapt to this new way of writing. But, those assumptions can lead to big problems.</p>
    <p class="body">In a poll conducted in a recent webinar[ii] where half of the participants indicated they were already using DITA, a full 70% indicated that they had no formal DITA training. Of those participants, nearly 60% were self-taught while the others had</p>
    <h2 class="h-section" style="margin-top:6px">SELECTING THE BEST TRAINING FOR YOUR NEEDS</h2>
    <p class="body">There are many training options available to learn about DITA. Selecting the best training for your team entails examining what it is you need to learn. Most DITA training courses cover the features and walk you through the structures and mechanics of the standard. These courses demonstrate how to markup content, but will often not teach you how to rethink and restructure your content to take advantage of DITA’s features. Consider the differences between structured writing and structured markup.</p>
  </div>
  <div class="page-photo" role="img" aria-label="Photo: one hand holding red gears beside a head silhouette made of blue gears against a cloudy sky"></div>
  <svg class="footer" viewBox="0 0 350 19" aria-hidden="true">
    <polygon points="0,0 52,0 66,19 0,19" fill="var(--navy)"/>
    <polygon points="222,0 350,0 350,19 208,19" fill="var(--navy)"/>
  </svg>
  <span class="footer-num">2</span>
  <span class="footer-url">www.quillmarrowgroup.com</span>
</section>

</body>
</html>
```